Buch-/E-Book-Cover Existenzgründer und Gründungsinteressierte
Zielgruppe
Es geht um eine Buchcover mit dem Titel 'Wolkenhafen erkunden'; Zielgruppe sind Existenzgründer und Gründungsinteressierte
Aufgabenstellung
Das Buchcover sollte modern und frisch gestaltet werden, eine grobe Skizze ist beigefügt, unten rechts soll das Verlagslogo (klein) platziert werden
Haupttext „Wolkenhafen erkunden“ soll auffallend, vielleicht als Wortmarke, gestaltet werden – er sollte einen Wiedererkennungswert haben
Auf der Frontseite des Covers sollten auch die Schlüsselwörter zu den Hauptkapiteln integriert werden (siehe Idee Skizze), damit der Leser auf den 1. Blick einen Eindruck über die Inhalte des Ratgebers gewinnt
Format: Das Taschenbuch soll im Hochformat (13,97 cm x 21,59 cm, Bindung links, Veltrano Quill Print Service) erscheinen und das Buch hat ca. 190 Seiten. Das Cover soll ein Softcover (235g Chromokarton), 4/4 farbig sein.

```html
<!DOCTYPE html>
<html lang="de">
<head>
<meta charset="utf-8">
<title>Wolkenhafen erkunden – Buchcover</title>
<link rel="stylesheet" href="https://fonts.googleapis.com/css2?family=Russo+One&family=Roboto+Condensed:wght@400;700&family=Arimo&display=swap">
<style>
  :root {
    --cover-blue: #0e56a6;
    --cover-blue-deep: #0a4690;
    --accent-yellow: #ffe82a;
    --ink-blue: #1a3f8c;
    --text-white: #ffffff;
    --photo-top: #0e56a6;
    --photo-mid: #4a6a9a;
    --photo-low: #9aa7b8;
  }
  * { margin: 0; padding: 0; box-sizing: border-box; }
  html, body { width: 1200px; height: 864px; overflow: hidden; background: #ffffff; }
  .cover { position: relative; width: 1200px; height: 864px; background: var(--cover-blue); overflow: hidden; }

  .back-cover { position: absolute; left: 0; top: 0; width: 560px; height: 864px; background: var(--cover-blue); }
  .blurb { position: absolute; left: 54px; top: 96px; width: 450px; color: var(--text-white);
    font-family: "Arimo", Arial, sans-serif; font-size: 14.2px; line-height: 1.5; }
  .blurb p + p { margin-top: 21px; }

  .spine { position: absolute; left: 560px; top: 0; width: 80px; height: 864px; background: var(--accent-yellow); }
  .spine-title { position: absolute; left: 40px; top: 168px; transform-origin: 0 0; transform: rotate(90deg) translateY(-50%);
    white-space: nowrap; font-family: "Russo One", sans-serif; font-size: 31px; letter-spacing: 1px; color: var(--ink-blue); }

  .front-cover { position: absolute; left: 640px; top: 0; width: 560px; height: 864px; background: var(--cover-blue); }
  .cover-photo { position: absolute; left: 0; top: 560px; width: 560px; height: 304px;
    background: linear-gradient(180deg, var(--photo-top) 0%, var(--photo-mid) 35%, var(--photo-low) 100%); }
  .title { position: absolute; left: 35px; top: 50px; font-family: "Russo One", sans-serif; font-size: 50px;
    line-height: 1.2; letter-spacing: 2px; color: var(--text-white); }
  .subtitle { position: absolute; left: 37px; top: 196px; font-family: "Roboto Condensed", sans-serif; font-weight: 700;
    font-size: 25px; color: var(--accent-yellow); }
  .contents { position: absolute; left: 37px; top: 310px; width: 520px; font-family: "Roboto Condensed", sans-serif;
    font-size: 26px; line-height: 1.4; color: var(--text-white); }
  .contents-lead { margin-bottom: 4px; }
  .topic-columns { display: flex; gap: 18px; }
  .topic-list { list-style: none; }
  .topic-list:first-child { width: 208px; }
  .topic-list li { position: relative; padding-left: 20px; }
  .topic-list li::before { content: ""; position: absolute; left: 1px; top: 12px; width: 14px; height: 14px; border-radius: 50%;
    border: 2px solid var(--text-white); background: radial-gradient(circle, var(--text-white) 0 3px, transparent 3.5px); }

  .author-band { position: absolute; left: 2px; top: 795px; width: 450px; height: 42px; background: var(--accent-yellow);
    display: flex; align-items: center; justify-content: center;
    font-family: "Roboto Condensed", sans-serif; font-weight: 700; font-size: 25px; color: var(--ink-blue); }
  .publisher { position: absolute; left: 458px; top: 760px; width: 96px; height: 76px; background: var(--cover-blue-deep);
    display: flex; flex-direction: column; align-items: center; justify-content: center; gap: 6px;
    font-family: "Roboto Condensed", sans-serif; font-weight: 700; font-size: 15px; line-height: 1.05;
    color: var(--text-white); text-align: center; text-transform: uppercase; }
  .publisher-mark { width: 14px; height: 14px; background: var(--accent-yellow); }
</style>
</head>
<body>
<div class="cover">
  <section class="back-cover">
    <div class="blurb">
      <p>Lorem ipsum dolor sit amet, consectetur adipiscing elit, sed do eiusmod tempor incididunt ut labore et dolore magna aliqua. Amet dictum sit amet justo donec enim. Eget arcu dictum varius duis at consectetur. Quis hendrerit dolor magna eget. Nascetur ridiculus mus mauris vitae.</p>
      <p>Lorem ipsum dolor sit amet, consectetur adipiscing elit, sed do eiusmod tempor incididunt ut labore et dolore magna aliqua. Sed lectus vestibulum mattis ullamcorper velit sed ullamcorper morbi tincidunt. Ultricies mi eget mauris pharetra et. Lectus quam id leo in vitae turpis massa sed. Laoreet suspendisse interdum consectetur libero id faucibus. Morbi tristique senectus et netus et malesuada fames. Donec adipiscing tristique risus nec feugiat in fermentum posuere urna. Diam volutpat commodo sed egestas egestas fringilla phasellus faucibus.</p>
      <p>Lorem ipsum dolor sit amet, consectetur adipiscing elit, sed do eiusmod tempor incididunt ut labore et dolore magna aliqua. Egestas dui id ornare arcu odio ut sem nulla. Urna nunc id cursus metus.</p>
    </div>
  </section>

  <section class="spine">
    <div class="spine-title">WOLKENHAFEN ERKUNDEN</div>
  </section>

  <section class="front-cover">
    <div class="cover-photo" role="img" aria-label="Foto: Geschäftsbesprechung in einem Büro, eine Frau präsentiert vor einem Bildschirm, Kollegen sitzen am Tisch"></div>
    <h1 class="title">WOLKENHAFEN<br>ERKUNDEN</h1>
    <p class="subtitle">Existenzgründung für Kleinunternehmen</p>
    <div class="contents">
      <p class="contents-lead">Alles über:</p>
      <div class="topic-columns">
        <ul class="topic-list">
          <li>Behördengänge</li>
          <li>Rechtsform</li>
          <li>(digitale) Büroorganisation</li>
          <li>Buchhaltung und steuern</li>
        </ul>
        <ul class="topic-list">
          <li>Finanzierung und Fördelmittel</li>
          <li>Businessplan</li>
          <li>Versicherungen</li>
          <li>Bonus: Online-Trainings und Vorlagen</li>
        </ul>
      </div>
    </div>
    <div class="author-band">von Jonas Albrecht</div>
    <div class="publisher"><span class="publisher-mark"></span><span>Ruderklar<br>Verlag</span></div>
  </section>
</div>
</body>
</html>
```